Beacon Advisory Website

I currently have a website www.beaconadvisoryinc.example. We are a IT Consulting Company. Our website will pretty much tell out our services. I am looking to enhance my website and make it look more professional. Looking for very classy and Contemporary look and design for my website.

Industry/Entity Type

It Company

```html
<!DOCTYPE html>
<html lang="en">
<head>
<meta charset="utf-8">
<title>Beacon Advisory</title>
<link href="https://fonts.googleapis.com/css2?family=Open+Sans:wght@400;600;700&display=swap" rel="stylesheet">
<style>
  :root {
    --navy: #1a3f7a;
    --grey-nav: #8a8a8a;
    --white: #ffffff;
    --hero-dark: #2b2b2b;
    --hero-mid: #4a4a4a;
    --accent-blue: #1b67b3;
    --band-blue: #00a9e2;
  }
  * { margin: 0; padding: 0; box-sizing: border-box; }
  html, body { width: 1200px; height: 965px; overflow: hidden; }
  body { font-family: "Open Sans", sans-serif; background: var(--white); position: relative; }

  .site-header { position: absolute; top: 0; left: 0; width: 1200px; height: 113px; background: var(--white); }
  .brand { position: absolute; left: 138px; top: 38px; display: flex; align-items: center; gap: 12px; }
  .brand-mark { width: 34px; height: 34px; background: var(--accent-blue); }
  .brand-name { font-size: 26px; font-weight: 700; color: var(--navy); letter-spacing: 0.5px; }

  .main-nav { position: absolute; top: 48px; left: 463px; display: flex; gap: 21px; }
  .main-nav a { font-size: 16px; font-weight: 600; color: var(--navy); text-decoration: none; letter-spacing: 0.2px; }
  .main-nav a.is-current { color: var(--grey-nav); margin-right: 4px; }

  .hero { position: absolute; top: 113px; left: 0; width: 1200px; height: 635px;
    background: radial-gradient(ellipse at 70% 75%, #5a5a5a 0%, var(--hero-mid) 30%, var(--hero-dark) 75%); }
  .hero-copy { position: absolute; top: 123px; left: 0; width: 1200px; text-align: center;
    font-size: 24px; font-weight: 700; line-height: 33px; color: var(--white);
    text-shadow: 0 1px 3px rgba(0,0,0,0.6); }
  .hero-copy .highlight { color: var(--accent-blue); font-weight: 600; }
  .btn-learn { position: absolute; left: 510px; top: 344px; width: 176px; height: 70px;
    border: 1px solid rgba(255,255,255,0.75); border-radius: 3px; color: var(--white);
    font-size: 20px; font-weight: 700; display: flex; align-items: center; justify-content: center;
    text-decoration: none; }

  .services { position: absolute; top: 748px; left: 0; width: 1200px; height: 217px; background: var(--band-blue); }
  .service { position: absolute; top: 26px; text-align: center; color: var(--white); }
  .service h2 { font-size: 25px; font-weight: 700; line-height: 32px; }
  .service p { font-size: 16px; line-height: 26px; margin-top: 2px; }
  .service .read-more { display: block; font-size: 16px; font-weight: 700; color: var(--white);
    text-decoration: none; margin-top: 4px; }
  .service-consulting { left: 54px; width: 300px; }
  .service-consulting .read-more { padding-left: 144px; }
  .service-staff { left: 410px; width: 334px; }
  .service-staff .read-more { padding-left: 144px; }
  .service-offshore { left: 808px; width: 348px; top: 27px; }
  .service-offshore .read-more { padding-left: 144px; margin-top: 2px; }
</style>
</head>
<body>
  <header class="site-header">
    <div class="brand">
      <span class="brand-mark"></span>
      <span class="brand-name">Beacon Advisory</span>
    </div>
    <nav class="main-nav">
      <a href="#" class="is-current">COMPANY</a>
      <a href="#">SERVICES</a>
      <a href="#">SOLUTIONS</a>
      <a href="#">RESOURCES</a>
      <a href="#">CAREER</a>
      <a href="#">CONTACT US</a>
    </nav>
  </header>

  <section class="hero" role="img" aria-label="Blurred photo of a person writing at a desk beside a keyboard">
    <p class="hero-copy">
      Today’s IT market is a dynamic, fast-paced industry, with ever-increasing demands.<br>
      Meeting these demands for over 25 years, <span class="highlight">Beacon Advisory</span> maintains a global presence,<br>
      aggressively recruiting expertly qualified <span class="highlight">IT and Management Professionals</span> from around the world<br>
      and cultivating key partnerships with corporations to understand their business models<br>
      end-to-end, with a goal of delivering exceptional client service and ensuring a consistent delivery<br>
      of the talent needed to drive results.
    </p>
    <a href="#" class="btn-learn">Learn More</a>
  </section>

  <section class="services">
    <div class="service service-consulting">
      <h2>Consulting</h2>
      <p>Beacon Advisory has certified professional consultants to work with you to help increase the business by providing IT services …</p>
      <a href="#" class="read-more">Read more</a>
    </div>
    <div class="service service-staff">
      <h2>Staff Augmentation</h2>
      <p>For years Beacon Advisory as been offering our customers the ability to augment their existing staff …</p>
      <a href="#" class="read-more">Read more</a>
    </div>
    <div class="service service-offshore">
      <h2>Offshore</h2>
      <p>Our Offshore development model has a unique distinction of providing efficient soft-ware solutions …</p>
      <a href="#" class="read-more">Read more</a>
    </div>
  </section>
</body>
</html>
```